quickpine website

I need the graphics and images created for a web site. I have settled on a layout but are open to alternatives

I have already purchased the images I want to use.

I want the graphics/design to really give the web site a lift without deviating from the core concept (which is lots of white space, clean looking)

I have further files to upload for use (another 4).

The link to the current web site that requires re-skinning is: http://www.tarvinmarketing.com.au/cgi-bin/xmlweb.cgi/scriptlet/quickpine?cms_section=quickpine&cms_name=home
Updates

I forgot to mention that I would the design elements of the various text boxes down the right hand side and along the bottom of the page to be improved.  At the moment they look very one dimensional and boring.

Thanks

All files have now been uploaded.

Hi Guys
Some great designs are coming through.  I thought I would share elements that I like for each for those of you who are prepared to tweek their submissions.

Design ID 27087
1. Used used the proper logo file supplied
2. Like the use of images and design of the various text boxes down the right hand side of the page
3.  I like the footer - but would maybe change some of the images used
4.  I like the navigation bar

Design ID 27265
1. Like the placement of icons up the top.  I think this concept would work if there were maybe three other icons up there as well

Design ID 27266
1.  Like the design elements of the various text boxes down the right hand side of the page
2.  Like the grey background strip down the right hand side of page

Key thing I would like improved:
1.  The style and use of text in the header/banner.  I also think it looks a little one dimensional

Thanks

Rgds
Dale

Target Market(s)

SME businesses

Number of Pages Required

1 page

Requirements
Must have
• 1. Header/Banner must replicate concept provided
2. Please check out this web site as it is the design inspiration and should heavily influence the final design (use of colour etc) - www.plovinstudio.com

```html
<!DOCTYPE html>
<html lang="en">
<head>
<meta charset="utf-8">
<title>quickpine marketing</title>
<link href="https://fonts.googleapis.com/css2?family=Signika:wght@400;600&family=Noto+Sans:wght@400;700&family=Arimo:wght@400;700&family=Didact+Gothic&display=swap" rel="stylesheet">
<style>
:root{
  --blue:#0a78c2;
  --blue-bright:#1c9be0;
  --sky-top:#2d98dc;
  --sky-bottom:#67c0ee;
  --band:#1386d2;
  --green:#2fb52c;
  --green-dark:#1f9a1e;
  --ink:#333;
  --panel-border:#3ab0e6;
  --strip:#eef0f2;
  --placeholder-top:#f1f2f3;
  --placeholder-bottom:#cfd3d7;
  --white:#fff;
}
*{box-sizing:border-box;margin:0;padding:0}
html,body{width:868px;height:1200px;overflow:hidden;background:var(--white)}
body{position:relative;font-family:"Noto Sans",sans-serif;color:var(--ink)}
.abs{position:absolute}

/* header */
.site-header{left:0;top:0;width:868px;height:81px;background:linear-gradient(#fff,#f3f6f9)}
.brand{left:89px;top:12px;display:flex;align-items:center;gap:6px}
.brand-dot{width:46px;height:46px;border-radius:50%;background:var(--blue-bright)}
.brand-name{font-family:"Signika",sans-serif;font-weight:600;font-size:30px;color:var(--blue)}
.main-nav{left:0;top:0;width:868px;height:81px;font-family:"Signika",sans-serif;font-weight:600;font-size:12px;color:var(--blue)}
.main-nav a{position:absolute;top:30px;color:inherit;text-decoration:none;white-space:nowrap}
.main-nav a.nav-home{top:24px;left:336px;width:50px;text-align:center;background:var(--blue-bright);color:#fff;padding:6px 0;border-radius:3px}
.nav-home::after{content:"";position:absolute;left:50%;bottom:-7px;margin-left:-5px;border:5px solid transparent;border-top:4px solid var(--blue-bright);border-bottom:0}

/* hero */
.hero{left:0;top:81px;width:868px;height:268px;background:linear-gradient(var(--sky-top),var(--sky-bottom) 70%,#4fb0e6)}
.hero-rule{left:0;top:349px;width:868px;height:6px;background:var(--band)}
.call-banner{left:485px;top:82px;width:299px;height:43px;background:linear-gradient(var(--green),var(--green-dark));clip-path:polygon(30px 0,100% 0,100% 100%,30px 100%,0 50%);color:#fff;font-family:"Signika",sans-serif;font-weight:600;font-size:20px;line-height:43px;text-align:right;padding-right:16px}
.hero-title{left:97px;top:96px;font-family:"Signika",sans-serif;font-weight:600;font-size:34px;color:#444}
.hero-sub{left:96px;top:151px;width:660px;font-family:"Didact Gothic",sans-serif;font-size:15.6px;line-height:18px;color:#fff}
.hero-art{border-radius:10px}
.hero-label{font-family:"Signika",sans-serif;font-weight:600;font-size:22.5px;line-height:26px;color:#444}

/* content */
.side-strip{left:522px;top:355px;width:346px;height:697px;background:linear-gradient(90deg,#e3e6e9,var(--strip) 8px,#fff 60px)}
.intro{left:89px;top:374px;width:418px;font-size:10.3px;line-height:12.2px;letter-spacing:.45px;color:#444}
.intro h1{font-family:"Signika",sans-serif;font-size:13px;color:var(--blue);margin-bottom:19px;letter-spacing:.2px}
.intro h2{font-size:10.6px;color:var(--blue);font-weight:700;letter-spacing:.2px}
.intro p{margin-bottom:18px}
.intro p.tight{margin-bottom:12px}
.service{left:89px;width:416px;border-bottom:1.5px dotted var(--blue-bright)}
.service-img{position:absolute;left:1px;width:73px;background:linear-gradient(var(--placeholder-top),var(--placeholder-bottom))}
.service-body{position:absolute;left:85px;right:0}
.service h3{font-size:11px;color:var(--blue);font-weight:700;margin-bottom:2px;letter-spacing:.2px}
.service p{font-size:10.4px;line-height:12.2px;letter-spacing:.45px;color:#444}
.read-more{position:absolute;right:3px;font-size:10.5px;font-weight:700;color:var(--blue)}

/* sidebar */
.panel{left:539px;width:241px;border:2px solid var(--panel-border);border-radius:8px;background:#fff;box-shadow:2px 2px 3px rgba(0,0,0,.18);font-family:"Arimo",sans-serif}
.panel-head{position:absolute;left:43px;top:9px;font-family:"Signika",sans-serif;font-weight:600;font-size:12.5px;color:#444}
.panel-icon{position:absolute;left:10px;top:6px;width:22px;height:22px;border-radius:4px}
.field-label{position:absolute;left:11px;font-size:8.5px;color:#333}
.field{position:absolute;left:83px;width:144px;height:16px;border:1px solid #999;background:#fff}
.btn{position:absolute;left:83px;width:144px;height:17px;background:linear-gradient(#4cbbed,#1c9be0);color:#fff;font-size:8.5px;text-align:center;line-height:17px}
.plain-list{position:absolute;left:11px;list-style:none;font-size:8.3px;line-height:13px;color:#333}
.media-list{position:absolute;left:11px;list-style:none;font-size:8.3px;line-height:13px}
.media-list li{color:#222;text-decoration:underline}
.media-list li::before{content:"";display:inline-block;width:4px;height:4px;border-radius:50%;background:var(--blue-bright);margin-right:6px;vertical-align:middle}
.more-media{position:absolute;right:10px;font-size:8.3px;color:var(--blue)}
.video{left:552px;top:865px;width:211px;height:170px;background:linear-gradient(#4a4a4a,#1d1d1d)}
.video-title{position:absolute;left:47px;top:5px;background:#111;padding:2px 4px;font-family:"Signika",sans-serif}
.video-title b{display:block;font-size:13px;color:#4cb8ef}
.video-title span{font-size:8px;color:#fff}
.video-title span em{font-style:normal;color:#4cb8ef}
.video-avatar{position:absolute;left:7px;top:6px;width:35px;height:35px;background:#8fd0f2}
.video-bar{position:absolute;left:7px;bottom:4px;width:197px;height:28px;background:rgba(0,0,0,.6);border-radius:3px}
.video-time{position:absolute;left:55px;top:-6px;background:#fff;color:#111;font-size:7px;padding:0 2px}
.video-track{position:absolute;left:62px;top:13px;width:86px;height:4px;border:1px solid #888}

/* promo band */
.promo{left:0;top:1052px;width:868px;height:99px;background:linear-gradient(#2aa5e8,var(--band))}
.promo-col{top:1052px;height:99px;border-right:1px solid rgba(255,255,255,.25)}
.promo-icon{position:absolute;width:44px;height:44px;border-radius:50%;background:rgba(255,255,255,.35)}
.promo-text{position:absolute;font-family:"Signika",sans-serif;font-weight:600;font-size:11px;line-height:13px;color:#fff}
.promo-link{position:absolute;font-family:"Signika",sans-serif;font-size:11px;color:#fff}

/* footer */
.site-footer{left:0;top:1163px;width:868px;border-top:1px solid #ddd;text-align:center;font-family:"Arimo",sans-serif;font-size:7.5px;line-height:10.5px;color:#333;padding-top:4px}
</style>
</head>
<body>

<header class="abs site-header">
  <div class="abs brand"><span class="brand-dot"></span><span class="brand-name">quickpine</span></div>
  <nav class="abs main-nav">
    <a class="nav-home">Home</a>
    <a style="left:395px">What We're Working On</a>
    <a style="left:542px">About Us</a>
    <a style="left:615px">Media</a>
    <a style="left:664px">Blog</a>
    <a style="left:713px">Contact Us</a>
  </nav>
</header>

<section class="abs hero"></section>
<div class="abs hero-rule"></div>
<div class="abs call-banner">Call Now on 1300 555 019</div>
<h1 class="abs hero-title">Reshaping Business</h1>
<p class="abs hero-sub">quickpine is a marketing agency specialising in marketing campaign design &amp; execution<br>using traditional and digital media</p>
<div class="abs hero-art" role="img" aria-label="Radio tower icon with red signal waves" style="left:100px;top:210px;width:98px;height:109px;background:linear-gradient(#3a8fcc,#2a6f9f)"></div>
<div class="abs hero-label" style="left:222px;top:236px">ONLINE DIGITAL<br>SOLUTION</div>
<div class="abs hero-art" role="img" aria-label="Retro television icon with antenna" style="left:481px;top:212px;width:89px;height:107px;background:linear-gradient(#3a8fcc,#1e5f8f)"></div>
<div class="abs hero-label" style="left:591px;top:236px">VIDEO<br>PRODUCTION</div>

<div class="abs side-strip"></div>

<main class="abs intro">
  <h1>Quickpine™ Marketing</h1>
  <h2 style="margin-bottom:12px">At quickpine marketing we’re reshaping business and building brands.</h2>
  <p style="margin-bottom:24px">We’re helping businesses like yours build their customer base and penetrate new markets.  Quickpine achieve this through strategic market campaign design and execution using a combination of traditional and digital media.</p>
  <h2>We’re your outsourced marketing department</h2>
  <p class="tight">As your outsourced marketing managers, quickpinespecialise in providing marketing strategies, brand &amp; logo development, public relations campaigns, advertising strategies, social media strategies, web site design and online marketing strategies.</p>
  <h2>We cause gravity to your business</h2>
  <p>We’ll reposition your business in the marketplace so that it resonates with your target market.  We’ll then help you implement powerful online and offline lead generation and sales strategies.</p>
</main>

<article class="abs service" style="top:646px;height:68px">
  <div class="service-img" role="img" aria-label="Darts striking a target" style="top:4px;height:52px"></div>
  <div class="service-body"><h3>Campaign Design &amp; Execution</h3><p>Seeking a marketing plan that works? Learn more about how we implement our powerful marketing strategies.</p></div>
  <span class="read-more" style="top:46px">→ read more</span>
</article>
<article class="abs service" style="top:721px;height:68px">
  <div class="service-img" role="img" aria-label="Two businessmen looking upward" style="top:4px;height:52px;background:linear-gradient(#c9b9a0,#6e6256)"></div>
  <div class="service-body"><h3>Marketing &amp; PR Strategy</h3><p>Learn more about how we can help build your customer base and penetrate new markets.</p></div>
  <span class="read-more" style="top:46px">→ read more</span>
</article>
<article class="abs service" style="top:796px;height:89px">
  <div class="service-img" role="img" aria-label="Painted colour stripes" style="top:4px;height:75px"></div>
  <div class="service-body"><h3>Marketing &amp; PR Strategy</h3><p>Quickpine design &amp; develop brochures, podcasts, vodcasts, advertisements, e-marketing campaigns, direct marketing &amp; promotional videos.</p></div>
  <span class="read-more" style="top:62px">→ read more</span>
</article>
<article class="abs service" style="top:892px;height:86px">
  <div class="service-img" role="img" aria-label="Light bulb with an at symbol filament" style="top:2px;height:78px"></div>
  <div class="service-body"><h3>Web Site Design &amp; Online Strategy</h3><p>What is your web site saying about your business? Learn how quickpine can build a new web site for your business that generates enquiries and convert sales.</p></div>
  <span class="read-more" style="top:59px">→ read more</span>
</article>

<aside>
  <section class="abs panel" style="top:374px;height:130px">
    <div class="panel-icon" role="img" aria-label="Bar chart icon" style="background:linear-gradient(#d7eefb,#8fc8ee)"></div>
    <h3 class="panel-head">FREE Marketing Assessment</h3>
    <span class="field-label" style="top:40px">Name</span><span class="field" style="top:35px"></span>
    <span class="field-label" style="top:61px">Company Name</span><span class="field" style="top:56px"></span>
    <span class="field-label" style="top:82px">Email</span><span class="field" style="top:77px"></span>
    <span class="btn" style="top:100px">Get your assessment</span>
  </section>
  <section class="abs panel" style="top:513px;height:115px">
    <div class="panel-icon" role="img" aria-label="Envelope icon" style="background:linear-gradient(#f7d77a,#8fc8ee)"></div>
    <h3 class="panel-head">Join our mailing list</h3>
    <span class="field-label" style="top:41px">Your Name</span><span class="field" style="top:36px"></span>
    <span class="field-label" style="top:62px">Email</span><span class="field" style="top:57px"></span>
    <span class="btn" style="top:81px">SUBSCRIBE</span>
  </section>
  <section class="abs panel" style="top:637px;height:103px">
    <div class="panel-icon" role="img" aria-label="Magnifying glass icon" style="background:linear-gradient(#d7eefb,#8fc8ee)"></div>
    <h3 class="panel-head">What are you looking for?</h3>
    <ul class="plain-list" style="top:33px">
      <li>I want to increase brandawareness</li>
      <li>I want greater lead generation</li>
      <li>I want a powerful online strategy</li>
      <li>I want to launch a new product or service</li>
      <li>I want a marketing overhaul</li>
    </ul>
  </section>
  <section class="abs panel" style="top:750px;height:104px">
    <div class="panel-icon" role="img" aria-label="Newspaper icon" style="background:linear-gradient(#eee,#999)"></div>
    <h3 class="panel-head">Recent Media</h3>
    <ul class="media-list" style="top:39px">
      <li>Podcast on 7 Ways to Improve your marketing</li>
      <li>Article on Why Most Marketing Fails</li>
      <li>Podcast interview with Lena Marsh</li>
    </ul>
    <span class="more-media" style="top:80px">→ more media item</span>
  </section>
  <div class="abs video" role="img" aria-label="Video player showing a presenter speaking on stage">
    <div class="video-avatar"></div>
    <div class="video-title"><b>Quick Pine</b><span>from <em>Dale Morrow</em></span></div>
    <div class="video-bar">
      <svg width="14" height="14" viewBox="0 0 14 14" style="position:absolute;left:17px;top:8px"><path d="M2 1L13 7L2 13Z" fill="#fff"/></svg>
      <span class="video-time">00:44</span>
      <span class="video-track"></span>
    </div>
  </div>
</aside>

<section class="abs promo"></section>
<div class="abs promo-col" style="left:0;width:272px">
  <div class="promo-icon" role="img" aria-label="Businessman with speech bubble" style="left:96px;top:10px"></div>
  <p class="promo-text" style="left:156px;top:19px;width:110px">Want a Web solution that actually Builds Business?</p>
  <span class="promo-link" style="left:198px;top:71px">learn more ▶</span>
</div>
<div class="abs promo-col" style="left:272px;width:185px">
  <div class="promo-icon" role="img" aria-label="Film strip" style="left:10px;top:19px"></div>
  <p class="promo-text" style="left:61px;top:19px;width:122px">Could a Video Presentation make all the Difference to Your Business?</p>
  <span class="promo-link" style="left:110px;top:71px">learn more ▶</span>
</div>
<div class="abs promo-col" style="left:457px;width:168px">
  <div class="promo-icon" role="img" aria-label="Information sign" style="left:8px;top:19px;background:#4a90e2"></div>
  <p class="promo-text" style="left:55px;top:25px;width:110px">Feel Like You're Not in Control of Your Business?</p>
  <span class="promo-link" style="left:92px;top:71px">learn more ▶</span>
</div>
<div class="abs promo-col" style="left:625px;width:243px;border-right:0">
  <div class="promo-icon" role="img" aria-label="Sales team figures" style="left:10px;top:20px"></div>
  <p class="promo-text" style="left:63px;top:25px;width:88px">Looking to Fine Tune Your Sales Team?</p>
  <span class="promo-link" style="left:81px;top:71px">learn more ▶</span>
</div>

<footer class="abs site-footer">
  Copyright © quickpine 2009<br>
  Home . What We're Working On . About Us . Media . Blog . Contact Us
</footer>

</body>
</html>
```